Graphic Design for a block-note A4 size

We need a graphic design for a simple block-note A4 size. The product consists of 50 sheets in VERTICAL A4 (21x29,7cm) size, simply glued on top, without cover. We would like to have proposals with double application: one for home users without a logo and one for professionals with an area "put your logo here".
The graphics should be simple and attractive, elegant and pleasant to keep on your desk.
The block-notes may have standard squares (5 or 10 mm) or stripes (10 mm spaced) on the background to make the writing easy.
Feel free to use your creativity, the only limit is the CMYK color space.

We will upload some block-note simple templates and 3D sample images to help you.

• The graphics should be simple and attractive, elegant and pleasant to keep on your desk.

• The block-notes may have standard squares (5 or 10 mm) or stripes (10 mm spaced) on the background to make the writing easy.

```html
<!DOCTYPE html>
<html lang="en">
<head>
<meta charset="utf-8">
<title>A4 Block-Note Sheet – Butterfly Meadow</title>
<link rel="stylesheet" href="https://fonts.googleapis.com/css2?family=Lato:wght@400&display=swap">
<style>
  :root {
    --backdrop: #f4f4f2;
    --sheet: #f7f7f5;
    --sheet-edge: #e3e3e0;
    --grid-line: #c9c9c6;
    --butterfly-peach: #f3c7ae;
    --butterfly-pink: #f6d3cf;
    --leaf-violet: #c9a9d8;
    --leaf-green: #a9d7a3;
    --leaf-yellow: #f1e59d;
    --wave-green: #9ed97f;
    --wave-light: #d7efc8;
  }
  * { margin: 0; padding: 0; box-sizing: border-box; }
  html, body {
    width: 1200px;
    height: 1200px;
    overflow: hidden;
    background: var(--backdrop);
    font-family: "Lato", sans-serif;
  }
  .canvas {
    position: relative;
    width: 1200px;
    height: 1200px;
  }
  .notepad-sheet {
    position: absolute;
    left: 211px;
    top: 50px;
    width: 778px;
    height: 1100px;
    background: var(--sheet);
    box-shadow: 0 0 0 1px var(--sheet-edge), 0 6px 18px rgba(0,0,0,0.06);
  }
  .notepad-sheet svg {
    display: block;
    width: 100%;
    height: 100%;
  }
</style>
</head>
<body>
<main class="canvas">
  <section class="notepad-sheet" aria-label="A4 notepad sheet with 10 mm squares">
    <svg viewBox="0 0 778 1100" xmlns="http://www.w3.org/2000/svg">
      <defs>
        <pattern id="square-grid" x="37" y="37" width="37" height="37" patternUnits="userSpaceOnUse">
          <path d="M37 0 V37 M0 37 H37" fill="none" stroke="var(--grid-line)" stroke-width="1" stroke-dasharray="3 2"/>
        </pattern>
        <radialGradient id="butterfly-glow" cx="50%" cy="50%" r="50%">
          <stop offset="0%" stop-color="var(--butterfly-peach)" stop-opacity="0.55"/>
          <stop offset="60%" stop-color="var(--butterfly-pink)" stop-opacity="0.3"/>
          <stop offset="100%" stop-color="var(--butterfly-pink)" stop-opacity="0"/>
        </radialGradient>
        <radialGradient id="plant-glow" cx="50%" cy="50%" r="50%">
          <stop offset="0%" stop-color="var(--leaf-violet)" stop-opacity="0.55"/>
          <stop offset="45%" stop-color="var(--leaf-yellow)" stop-opacity="0.4"/>
          <stop offset="75%" stop-color="var(--leaf-green)" stop-opacity="0.3"/>
          <stop offset="100%" stop-color="var(--leaf-green)" stop-opacity="0"/>
        </radialGradient>
        <linearGradient id="wave-band" x1="0" y1="0" x2="0" y2="1">
          <stop offset="0%" stop-color="var(--wave-light)" stop-opacity="0"/>
          <stop offset="45%" stop-color="var(--wave-green)" stop-opacity="0.45"/>
          <stop offset="100%" stop-color="var(--wave-light)" stop-opacity="0.2"/>
        </linearGradient>
      </defs>

      <rect class="writing-grid" x="37" y="37" width="704" height="999" fill="url(#square-grid)"/>
      <rect x="37" y="37" width="704" height="999" fill="none" stroke="var(--grid-line)" stroke-width="1" stroke-dasharray="3 2"/>

      <ellipse class="butterfly-flight" role="img" aria-label="Illustration of pale peach and pink butterflies fluttering across the sheet"
               cx="430" cy="560" rx="230" ry="200" fill="url(#butterfly-glow)"/>

      <ellipse class="flowering-branch" role="img" aria-label="Illustration of a slender branch with pastel violet, yellow and green leaves"
               cx="610" cy="720" rx="200" ry="230" fill="url(#plant-glow)"/>

      <path class="meadow-wave" role="img" aria-label="Decorative band of fine green flowing wave lines"
            d="M0 930 C 120 880, 220 960, 340 940 C 470 915, 560 860, 778 800 L 778 1010 C 620 1040, 470 1000, 330 1040 C 200 1075, 90 1030, 0 1050 Z"
            fill="url(#wave-band)"/>
    </svg>
  </section>
</main>
</body>
</html>
```